Business Card Design Project

We need a Business Card for an Mechanical Engineering firm in Singapore. The design should be Modern & Technical looking, yet eye catching.

Our company deals in Cutting Tools & Machine Accessories for the Manufacturing Industries such as Oil & Gas, Aero Space, etc... For more information on our Company, you can either email me or view our website www.valtrion.com.sg.

We are trying to revamp our image to give our consumers a fresh new perspective to our company, so we welcome all ideas.

Industry/Entity Type

Business

Requirements
Must have
• Must incorporate New Company Logo into the card as shown in Uploaded file.

```html
<!DOCTYPE html>
<html lang="en">
<head>
<meta charset="utf-8">
<title>Valtrion Tools – Business Card</title>
<link rel="stylesheet" href="https://fonts.googleapis.com/css2?family=Arimo:wght@400&family=Orbitron:wght@500&display=swap">
<style>
  :root {
    --paper: #ffffff;
    --ink-name: #3a0a16;
    --band-light: #8e0f14;
    --band-dark: #4e0309;
    --contact-text: #ffffff;
    --brand: #8c1431;
    --shadow: rgba(0, 0, 0, 0.22);
  }
  * { margin: 0; padding: 0; box-sizing: border-box; }
  html, body { width: 1200px; height: 736px; overflow: hidden; background: var(--paper); }
  .card {
    position: relative;
    width: 1200px;
    height: 736px;
    background: var(--paper);
    overflow: hidden;
  }
  .name-shadow {
    position: absolute;
    left: 262px;
    top: 336px;
    width: 680px;
    height: 44px;
    background: radial-gradient(ellipse 50% 50% at 50% 20%, var(--shadow), rgba(0,0,0,0) 100%);
  }
  .holder-name {
    position: absolute;
    left: 0;
    right: 0;
    top: 268px;
    text-align: center;
    font-family: "Orbitron", sans-serif;
    font-weight: 500;
    font-size: 56px;
    letter-spacing: 4px;
    color: var(--ink-name);
    text-transform: uppercase;
  }
  .contact-band {
    position: absolute;
    left: 0;
    top: 590px;
    width: 1200px;
    height: 146px;
    background: linear-gradient(90deg, var(--band-light) 0%, #6a050c 45%, var(--band-dark) 70%, #7a0a10 100%);
  }
  .contact-details {
    position: absolute;
    left: 36px;
    top: 626px;
    font-family: "Arimo", sans-serif;
    font-size: 16.5px;
    line-height: 22.5px;
    color: var(--contact-text);
    list-style: none;
  }
  .brand-panel {
    position: absolute;
    left: 798px;
    top: 588px;
    width: 391px;
    height: 136px;
    background: var(--paper);
    display: flex;
    align-items: center;
    justify-content: center;
    gap: 14px;
  }
  .brand-dot {
    width: 30px;
    height: 30px;
    border-radius: 50%;
    background: var(--brand);
  }
  .brand-name {
    font-family: "Arimo", sans-serif;
    font-weight: 400;
    font-size: 38px;
    letter-spacing: 1px;
    color: var(--brand);
    text-transform: uppercase;
  }
</style>
</head>
<body>
  <main class="card">
    <div class="name-shadow"></div>
    <h1 class="holder-name">Marcus Hale</h1>

    <section class="contact-band">
    </section>
    <ul class="contact-details">
      <li>http://www.valtrion.com.sg, Email id: info@valtrion.com.sg</li>
      <li>Mob: 91 98472 61035</li>
      <li>Address: 42/7 Lane Street, Riverton, New Haven</li>
    </ul>

    <div class="brand-panel">
      <span class="brand-dot"></span>
      <span class="brand-name">Valtrion Tools</span>
    </div>
  </main>
</body>
</html>
```